Business Card Design

BrightHarbor is a fund management company that takes just four market positions a year. each position is linked to a big geopolitical and economic event happening in the world. So for example we may be buying gold mining stocks-these are the companies who dig the gold out of the ground, as all the gold is currently being bought by Asia, or buying the japanese stock market as this is one of the big stories of today.

I am looking for a logo that represents 'BrightHarbor'-the Bright Harbor.

I would like it to be small and sit to the left of the name of the company on the left hand side(I think!)on the top line of the business card please.

Industry/Entity Type

Mining

Contact Information for Business Card

BrightHarbor Capital management Ltd
41 Pellam Street
London E9T 2QN

Martin J Colby

Mob: 0(44)7823946250
Off: 0(44) 207 xxxx
email: mc@brightharbor-cm.example

```html
<!DOCTYPE html>
<html lang="en">
<head>
<meta charset="utf-8">
<title>BrightHarbor Investment management – Business Card</title>
<link rel="stylesheet" href="https://fonts.googleapis.com/css2?family=Carlito:ital,wght@1,700&display=swap">
<style>
  :root {
    --ink-blue: #1f1ff0;
    --card-bg: #ffffff;
    --page-bg: #ffffff;
  }
  html, body {
    margin: 0;
    padding: 0;
    width: 1200px;
    height: 702px;
    overflow: hidden;
    background: var(--page-bg);
  }
  .card {
    position: relative;
    width: 1200px;
    height: 702px;
    background: var(--card-bg);
    font-family: "Carlito", "Calibri", sans-serif;
    font-weight: 700;
    font-style: italic;
    color: var(--ink-blue);
  }
  .card p { margin: 0; position: absolute; white-space: nowrap; line-height: 1; }

  .brand-mark {
    position: absolute;
    left: 60px;
    top: 100px;
    display: flex;
    align-items: center;
    gap: 14px;
  }
  .brand-mark__dot {
    width: 46px;
    height: 46px;
    border-radius: 50%;
    background: var(--ink-blue);
  }
  .brand-mark__name {
    font-size: 34px;
    color: var(--ink-blue);
  }

  .company-name { left: 455px; top: 102px; font-size: 34px; }
  .person-title {
    left: 0; right: 0; top: 313px;
    text-align: center;
    font-size: 33px;
    text-decoration: underline;
    text-decoration-thickness: 2px;
    text-underline-offset: 4px;
    white-space: pre;
  }
  .address { left: 56px; top: 505px; font-size: 34px; }
  .mobile { left: 56px; top: 597px; font-size: 30px; }
  .email { right: 58px; top: 593px; font-size: 30px; }
</style>
</head>
<body>
  <main class="card">
    <div class="brand-mark">
      <span class="brand-mark__dot"></span>
      <span class="brand-mark__name">BrightHarbor</span>
    </div>

    <p class="company-name">BrightHarbor Investment management</p>
    <p class="person-title"> Martin J Colby - The Director </p>
    <p class="address">Address: 41 Pellam Street London</p>
    <p class="mobile">Mob: 0(44)7823946250</p>
    <p class="email">email: mc@brightharbor-cm.</p>
  </main>
</body>
</html>
```